Fennick Executive Search - New Business Card Design Project

We are an executive search firm called Fennick Executive Search based in the UK. We require a custom design for a business card. We're looking to convey a professional service to executives for executive search recruitment services. In terms of colours, we like dark blues and grays (maybe even silver incorporated somewhere if we go for a foiled type of card) but we're open to your artistic flare. See our current logo in attachments. We are totally open on design so long as the design is slick and professional.
Updates

Thanks for all your contributions of various designs. I have to say the quality of work has been amazing which is going to make our job quite difficult in the coming days on making a decision. Thanks to you all that have taken the time to submit designs thus far. We'll keep on reviewing and try to narrow down our selection as soon as possible.

Target Market(s)

Executive Search

Industry/Entity Type

Recruitment

Contact Information for Business Card

Fennick Executive Search,
Carefully Finding & Placing Senior Executives
Gordon Pellbury, Managing Director,
07823 906417
0117 486 7132
gordon@fennickexecutive.co.uk
fennickexecutive.co.uk
58 Lindmoor Court, Hatherley Road, Bristol, BS32 9QJ

Font styles to use
Sans Serif
Other font styles liked:
• Roboto (which is used in our logo)

Requirements
Must have
• Our logo (It has a subtle fade on it from #02071d at top to #333649 at bottom)
• The logo can be on one side or both sides
• Must be elegant and professional
• We have 2nd slogan CONSULT | INSPIRE | INNOVATE | DELIVER which can be incorporated into the card
Nice to have
• Use of blues and grey colours
• Compatible with similar styling to our website fennickexecutive.co.uk
Should not have
• Must not be overly brash
• Must not contain cartoon characters

```html
<!DOCTYPE html>
<html lang="en">
<head>
<meta charset="utf-8">
<title>Fennick Executive Search – Business Card</title>
<link href="https://fonts.googleapis.com/css2?family=Roboto:wght@300;400;500;700&display=swap" rel="stylesheet">
<style>
  :root {
    --navy-top: #02071d;
    --navy-bottom: #333649;
    --ink: #14182e;
    --grey-text: #5b5d66;
    --accent-blue: #3ea6ef;
    --white: #ffffff;
    --page-bg: #e6e7ea;
    --rule: #7a7c84;
  }
  * { margin: 0; padding: 0; box-sizing: border-box; }
  html, body {
    width: 1200px; height: 1000px; overflow: hidden;
    background: var(--page-bg);
    font-family: "Roboto", Arial, sans-serif;
  }
  .canvas { position: relative; width: 1200px; height: 1000px; }

  .card {
    position: absolute; left: 263px; width: 674px; height: 419px;
    box-shadow: 0 2px 8px rgba(0,0,0,.18);
  }

  /* Front */
  .card-front {
    top: 58px;
    background: linear-gradient(170deg, var(--navy-top) 0%, #1a1e36 55%, var(--navy-bottom) 100%);
    color: var(--white);
  }
  .brand-name {
    position: absolute; left: 149px; top: 136px;
    color: var(--white); line-height: 1; font-weight: 400;
  }
  .brand-name .brand-main { display: block; font-size: 72px; font-weight: 700; letter-spacing: .5px; }
  .brand-name .brand-sub { display: block; font-size: 38px; font-weight: 300; margin-top: 10px; letter-spacing: .3px; }
  .tagline {
    position: absolute; left: 150px; top: 258px;
    font-size: 18px; color: var(--accent-blue); font-weight: 400; letter-spacing: .2px;
  }
  .values {
    position: absolute; left: 0; right: 0; top: 365px;
    display: flex; justify-content: center; align-items: center; gap: 10px;
    font-size: 15px; letter-spacing: .4px; color: var(--white);
  }
  .values .dot { width: 6px; height: 6px; border-radius: 50%; background: var(--accent-blue); }

  /* Back */
  .card-back { top: 532px; background: var(--white); color: var(--ink); }
  .back-brand {
    position: absolute; right: 25px; top: 26px;
    display: flex; align-items: center; gap: 10px;
  }
  .back-brand .brand-square {
    width: 40px; height: 40px;
    background: linear-gradient(180deg, var(--navy-top), var(--navy-bottom));
  }
  .back-brand .brand-label { font-size: 14px; font-weight: 500; color: var(--ink); letter-spacing: .5px; line-height: 1.2; }

  .person { position: absolute; left: 24px; top: 196px; }
  .person-name { font-size: 23px; font-weight: 700; color: var(--ink); }
  .person-title { font-size: 17px; color: var(--grey-text); margin-top: 2px; }
  .divider { position: absolute; left: 24px; right: 25px; top: 264px; height: 1px; background: var(--rule); }

  .contact-list { position: absolute; left: 24px; top: 284px; list-style: none; }
  .contact-list li {
    display: flex; align-items: center; gap: 6px;
    font-size: 17px; color: var(--grey-text); height: 24.5px;
  }
  .contact-list svg { width: 15px; height: 15px; fill: var(--ink); flex: none; }

  .address {
    position: absolute; right: 25px; top: 330px; text-align: right;
    font-size: 17px; color: var(--grey-text); line-height: 24px; font-style: normal;
  }
</style>
</head>
<body>
<main class="canvas">

  <section class="card card-front" aria-label="Business card front">
    <h1 class="brand-name">
      <span class="brand-main">FENNICK</span>
      <span class="brand-sub">EXECUTIVE SEARCH</span>
    </h1>
    <p class="tagline">Carefully Finding &amp; Placing Senior Executives</p>
    <p class="values">
      <span>ADVISE</span><span class="dot"></span>
      <span>ENGAGE</span><span class="dot"></span>
      <span>EVOLVE</span><span class="dot"></span>
      <span>ACHIEVE</span>
    </p>
  </section>

  <section class="card card-back" aria-label="Business card back">
    <div class="back-brand">
      <span class="brand-square"></span>
      <span class="brand-label">FENNICK<br>EXECUTIVE SEARCH</span>
    </div>

    <div class="person">
      <h2 class="person-name">Gordon Pellbury</h2>
      <p class="person-title">Managing Director</p>
    </div>
    <div class="divider"></div>

    <ul class="contact-list">
      <li>
        <svg viewBox="0 0 16 16" aria-hidden="true"><path d="M4 1.5l2.2 2.8-1.3 1.6c.9 2 2.6 3.8 4.6 4.7l1.6-1.3 2.8 2.2-1.4 2.5C7.2 14 2 8.8 1.5 2.9z"/></svg>
        07823 906417
      </li>
      <li>
        <svg viewBox="0 0 16 16" aria-hidden="true"><path d="M4 1h8v4H4zM1.5 6h13v6H12v3H4v-3H1.5zM5.5 10v3.5h5V10z"/></svg>
        0117 486 7132
      </li>
      <li>
        <svg viewBox="0 0 16 16" aria-hidden="true"><path d="M1 3.5h14v9H1zM2.2 4.5L8 9l5.8-4.5v1.2L8 10.2 2.2 5.7z" fill-rule="evenodd"/></svg>
        gordon@fennickexecutive.co.uk
      </li>
      <li>
        <svg viewBox="0 0 16 16" aria-hidden="true"><path d="M8 1a7 7 0 100 14A7 7 0 008 1zm0 1.3c.8 0 1.7 1.5 2 3.7H6c.3-2.2 1.2-3.7 2-3.7zM2.4 7h2.5v2H2.4zm3.6 0h4v2H6zm5.1 0h2.5v2h-2.5zM6 10h4c-.3 2.2-1.2 3.7-2 3.7S6.3 12.2 6 10zM5 6H2.8a5.7 5.7 0 012.9-3.3C5.3 3.6 5.1 4.7 5 6zm6 0c-.1-1.3-.3-2.4-.7-3.3A5.7 5.7 0 0113.2 6zm-6 4c.1 1.3.3 2.4.7 3.3A5.7 5.7 0 012.8 10zm6 0h2.2a5.7 5.7 0 01-2.9 3.3c.4-.9.6-2 .7-3.3z"/></svg>
        fennickexecutive.co.uk
      </li>
    </ul>

    <address class="address">
      58 Lindmoor Court, Hatherley Road,<br>
      Bristol, BS32 9QJ
    </address>
  </section>

</main>
</body>
</html>
```